flat authentication

design an authentication plate and an authentication certificate

on both you need the Brolo vintage store logo
authentication plate size 10 * 7cm
color black transparent text
aluminum plate material
American vintage spirit in the years 1950 to 1960

an authentication certificate
page size 4
the text to put above is in the word file
color black white red blue golden
on the certificate I would like the round golden pastille (like a seal)

```html
<!DOCTYPE html>
<html lang="en">
<head>
<meta charset="utf-8">
<title>Certificate of Authenticity – Brolo vintage store</title>
<link rel="stylesheet" href="https://fonts.googleapis.com/css2?family=Bebas+Neue&family=Open+Sans:wght@400;600&display=swap">
<style>
  :root {
    --navy: #13304a;
    --red: #a30f24;
    --cream: #fbf0d6;
    --paper: #fdfcf5;
    --map-line: #e6e8e4;
    --ink: #1a1a1a;
    --title: #363a3c;
    --ribbon: #f3c2cf;
    --hatch: #cfd3d2;
    --gold: #e2a812;
    --gold-light: #f8d85a;
    --gold-dark: #b97e0a;
  }
  html, body {
    margin: 0;
    padding: 0;
    overflow: hidden;
    background: #ffffff;
  }
  .certificate {
    position: relative;
    width: 1200px;
    height: 836px;
    overflow: hidden;
    background: var(--paper);
    font-family: "Open Sans", Arial, sans-serif;
    color: var(--ink);
  }
  .certificate__map {
    position: absolute;
    left: 70px;
    top: 200px;
    width: 1060px;
    height: 520px;
    background: radial-gradient(ellipse at center, #f4f5f0 0%, var(--paper) 75%);
  }
  .certificate__hatch {
    position: absolute;
    top: 195px;
    width: 60px;
    height: 600px;
    background: linear-gradient(180deg, var(--hatch), #dfe2e0);
    opacity: 0.55;
  }
  .certificate__hatch--left { left: 0; }
  .certificate__hatch--right { right: 10px; }
  .certificate__border {
    position: absolute;
    left: 0;
    width: 1200px;
  }
  .certificate__border--top { top: 0; height: 215px; }
  .certificate__border--bottom { bottom: 0; height: 200px; }
  .certificate__ribbon {
    position: absolute;
    left: 250px;
    top: 190px;
    width: 680px;
    height: 82px;
  }
  .brand {
    position: absolute;
    left: 104px;
    top: 240px;
    display: flex;
    align-items: center;
    gap: 8px;
    font-family: "Open Sans", Arial, sans-serif;
    font-weight: 600;
    font-size: 22px;
    color: var(--navy);
  }
  .brand__dot {
    width: 16px;
    height: 16px;
    border-radius: 50%;
    background: var(--red);
  }
  .certificate__title {
    position: absolute;
    left: 0;
    width: 1180px;
    top: 196px;
    margin: 0;
    text-align: center;
    font-family: "Bebas Neue", Impact, sans-serif;
    font-weight: 400;
    font-size: 94px;
    letter-spacing: 4px;
    line-height: 1;
    color: var(--title);
  }
  .certificate__subtitle {
    position: absolute;
    left: 0;
    width: 1196px;
    top: 280px;
    margin: 0;
    text-align: center;
    font-family: "Bebas Neue", Impact, sans-serif;
    font-size: 27px;
    letter-spacing: 2.5px;
    color: var(--title);
  }
  .certificate__statement {
    position: absolute;
    left: 0;
    width: 1184px;
    top: 327px;
    margin: 0;
    text-align: center;
    font-size: 17px;
    line-height: 24px;
  }
  .details {
    position: absolute;
    left: 327px;
    top: 394px;
    margin: 0;
    padding: 0;
    list-style: none;
    font-size: 24px;
    line-height: 43px;
  }
  .details__gap { display: inline-block; width: 30px; }
  .signature {
    position: absolute;
    left: 800px;
    top: 628px;
    display: flex;
    align-items: baseline;
    font-size: 15px;
  }
  .signature__line {
    display: inline-block;
    width: 170px;
    border-bottom: 1px solid var(--ink);
  }
  .seal {
    position: absolute;
    left: 517px;
    top: 607px;
    width: 150px;
    height: 150px;
  }
</style>
</head>
<body>
<main class="certificate">
  <div class="certificate__map" role="img" aria-label="Faint outline map of the United States"></div>
  <div class="certificate__hatch certificate__hatch--left" role="img" aria-label="Diagonal line pattern edging"></div>
  <div class="certificate__hatch certificate__hatch--right" role="img" aria-label="Diagonal line pattern edging"></div>

  <svg class="certificate__border certificate__border--top" viewBox="0 0 1200 215" role="img" aria-label="Wavy red, cream and navy stripes above a starred navy band">
    <defs>
      <linearGradient id="stripes-top" x1="0" x2="1" y1="0" y2="0">
        <stop offset="0" stop-color="#a30f24"/>
        <stop offset="0.25" stop-color="#13304a"/>
        <stop offset="0.5" stop-color="#a30f24"/>
        <stop offset="0.75" stop-color="#13304a"/>
        <stop offset="1" stop-color="#a30f24"/>
      </linearGradient>
    </defs>
    <rect x="0" y="0" width="1200" height="175" fill="url(#stripes-top)"/>
    <path d="M0 175 C300 150 500 142 700 148 C900 154 1050 165 1200 170 L1200 210 C1050 200 900 192 700 190 C500 188 300 194 0 212 Z" fill="var(--navy)"/>
    <path d="M0 165 C300 140 500 132 700 138 C900 144 1050 155 1200 160 L1200 170 C1050 165 900 154 700 148 C500 142 300 150 0 175 Z" fill="var(--cream)"/>
  </svg>

  <svg class="certificate__ribbon" viewBox="0 0 680 82" aria-hidden="true">
    <polygon points="0,8 130,8 130,0 550,0 550,8 680,8 650,42 680,78 540,78 540,62 140,62 140,78 0,78 30,42" fill="var(--ribbon)" opacity="0.8"/>
  </svg>

  <div class="brand"><span class="brand__dot"></span><span>Brolo</span></div>

  <h1 class="certificate__title">Certificate</h1>
  <p class="certificate__subtitle">of authenticity</p>
  <p class="certificate__statement">This Certificate attest to the fact this original gas pump is genuine<br>and was restored by our craftsman.</p>

  <ul class="details">
    <li>Product:&nbsp;&nbsp; xxxx</li>
    <li>Origin of the product: xxxxx</li>
    <li>Model: xxxxxx</li>
    <li>Restoration Number:&nbsp;&nbsp; xxx<span class="details__gap"></span>Year: xxxx</li>
    <li>Restored in Belgium by our craftsman: xxxx</li>
  </ul>

  <div class="signature">Autorised signature:<span class="signature__line"></span></div>

  <svg class="certificate__border certificate__border--bottom" viewBox="0 0 1200 200" role="img" aria-label="Starred navy band above wavy red, cream and navy stripes">
    <defs>
      <linearGradient id="stripes-bottom" x1="0" x2="1" y1="0" y2="0">
        <stop offset="0" stop-color="#13304a"/>
        <stop offset="0.3" stop-color="#a30f24"/>
        <stop offset="0.55" stop-color="#13304a"/>
        <stop offset="0.8" stop-color="#a30f24"/>
        <stop offset="1" stop-color="#13304a"/>
      </linearGradient>
    </defs>
    <path d="M0 130 C250 110 420 60 600 45 C800 30 1000 70 1200 80 L1200 200 L0 200 Z" fill="url(#stripes-bottom)"/>
    <path d="M0 118 C250 95 420 20 600 12 C800 5 1000 50 1200 60 L1200 92 C1000 85 800 52 600 60 C420 70 250 140 0 150 Z" fill="var(--navy)"/>
    <path d="M0 150 C250 140 420 70 600 60 C800 52 1000 85 1200 92 L1200 102 C1000 95 800 62 600 70 C420 80 250 150 0 160 Z" fill="var(--cream)"/>
  </svg>

  <svg class="seal" viewBox="0 0 150 150" aria-hidden="true">
    <defs>
      <radialGradient id="seal-gold" cx="0.4" cy="0.35" r="0.7">
        <stop offset="0" stop-color="var(--gold-light)"/>
        <stop offset="0.6" stop-color="var(--gold)"/>
        <stop offset="1" stop-color="var(--gold-dark)"/>
      </radialGradient>
    </defs>
    <circle cx="75" cy="75" r="73" fill="url(#seal-gold)"/>
  </svg>
</main>
</body>
</html>
```